distributor of aftermarket auto electrical components

I am after business card design for my new company called
Summit Vehicle Supplies (SVS as the acronym). I will supplying automotive wiring components, basically from battery to headlight. I will be aiming to sell in the 4wd scene and to auto electricians. i am not worried which colours are used though i would like it to be dynamic.
Updates

sorry guys, i have add a mobile and e-mail address that will need to on there as well. Sorry for theĀ inconvenience.

sorry guys i had erred on my spelling with my e-mail. i have now fixed it in the brief

Target Market(s)

4wd industry, custom cars, RV, auto electricians

Industry/Entity Type

Electrical

Requirements
Must have
• Company Name
ABN number: 71 306 548 290
Director: Derek Holloway
M 0432 718 946
E dhollo@fernwire.com.au

```html
<!DOCTYPE html>
<html lang="en">
<head>
<meta charset="utf-8">
<title>Summit Vehicle Supplies – Business Card</title>
<link href="https://fonts.googleapis.com/css2?family=Antonio:wght@200&family=EB+Garamond:wght@400&display=swap" rel="stylesheet">
<style>
  :root {
    --backdrop: #151515;
    --card-dark: #262727;
    --card-glow: #3a3d3d;
    --lime: #b3d92c;
    --lime-deep: #7f9c1f;
    --ink-light: #f4f4f0;
  }
  * { margin: 0; padding: 0; box-sizing: border-box; }
  html, body {
    width: 1200px;
    height: 855px;
    overflow: hidden;
    background: var(--backdrop);
  }
  .canvas {
    position: relative;
    width: 1200px;
    height: 855px;
  }
  .card {
    position: absolute;
    left: 366px;
    width: 498px;
    height: 244px;
    overflow: hidden;
  }
  .card--front {
    top: 107px;
    background: radial-gradient(ellipse 60% 70% at 50% 30%, var(--card-glow) 0%, var(--card-dark) 75%);
  }
  .company-name {
    position: absolute;
    left: 0;
    right: 0;
    top: 96px;
    text-align: center;
    font-family: "Antonio", sans-serif;
    font-weight: 200;
    font-size: 40px;
    line-height: 44px;
    letter-spacing: 2px;
    font-variant: small-caps;
    color: var(--ink-light);
    white-space: nowrap;
  }
  .card--back {
    top: 451px;
    background: linear-gradient(180deg, #2c2d2d 0%, var(--card-dark) 100%);
  }
  .card__accent {
    position: absolute;
    left: 0;
    top: 0;
    width: 498px;
    height: 130px;
    background: linear-gradient(180deg, var(--lime) 0%, var(--lime-deep) 45%, rgba(38, 39, 39, 0) 100%);
  }
  .contact {
    position: absolute;
    left: 249px;
    top: 124px;
    font-family: "EB Garamond", serif;
    color: var(--ink-light);
  }
  .contact__name {
    font-size: 34px;
    line-height: 38px;
    font-weight: 400;
    white-space: nowrap;
  }
  .contact__role {
    font-size: 15px;
    line-height: 15px;
  }
  .contact__details {
    list-style: none;
    font-size: 13.5px;
    line-height: 16.5px;
    white-space: nowrap;
  }
</style>
</head>
<body>
<main class="canvas">
  <section class="card card--front">
    <h1 class="company-name">Summit Vehicle Supplies</h1>
  </section>

  <section class="card card--back">
    <div class="card__accent" role="img" aria-label="Decorative lime green wave band across the top of the card"></div>
    <div class="contact">
      <h2 class="contact__name">Derek Holloway</h2>
      <p class="contact__role">Director</p>
      <ul class="contact__details">
        <li>abn: 71&nbsp;&nbsp;306&nbsp;&nbsp;548&nbsp;&nbsp;290</li>
        <li>m: 0432&nbsp;&nbsp;718&nbsp;&nbsp;946</li>
        <li>e-mail: dhollo@fernwire.com.au</li>
      </ul>
    </div>
  </section>
</main>
</body>
</html>
```